Store Promo Card (already have logo!)

I need a card design (single side) for my online women’s gift shop containing a promotional code to be placed in bags for attendees at an event. I’m flexible on both shape and sizing, but perhaps a 4x6 card.
—It should contain my attached logo, my website (www.corvidtpq.com), and my Instagram handle (@corvidtpq) and promotion language such as “15% off your purchase with code: MIRVOL”.
—I think I would like my logo to be large.
—It should be clean, simple and modern in design and should use the colors from my logo.
—I would like about 3-5 product pictures depending on design.
Target Market(s)
Women ages 30 to 60
Industry/Entity Type
Retail Upscale Gift
Look and feel

```html
<!DOCTYPE html>
<html lang="en">
<head>
<meta charset="utf-8">
<title>Corvid Promo Cards</title>
<link rel="stylesheet" href="https://fonts.googleapis.com/css2?family=Italiana&family=Great+Vibes&family=Montserrat:wght@400;700;800&display=swap">
<style>
  :root {
    --blush: #ecd0ca;
    --slate: #5d5e60;
    --paper: #ffffff;
    --backdrop: #f3f3f2;
    --slipper: #cdb9c4;
  }
  html, body {
    margin: 0;
    padding: 0;
    width: 1200px;
    height: 1000px;
    overflow: hidden;
    background: var(--backdrop);
  }
  .canvas { position: relative; width: 1200px; height: 1000px; }
  .promo-card {
    position: absolute;
    width: 433px;
    height: 288px;
    box-shadow: 0 4px 10px rgba(0,0,0,0.18);
    display: block;
  }
  .card-split   { left: 103px; top: 152px; }
  .card-product { left: 665px; top: 152px; }
  .card-circle  { left: 103px; top: 560px; }
  .card-bold    { left: 665px; top: 560px; }

  .display   { font-family: "Italiana", serif; fill: var(--slate); }
  .script    { font-family: "Great Vibes", cursive; fill: var(--slate); }
  .brand-name { font-family: "Montserrat", sans-serif; font-weight: 700; fill: var(--slate); letter-spacing: 2px; }
  .on-dark   { fill: var(--paper); }
  .contact   { font-family: "Montserrat", sans-serif; font-size: 11px; fill: var(--slate); }
  .headline  { font-family: "Montserrat", sans-serif; font-weight: 800; fill: var(--paper); }
</style>
</head>
<body>
<main class="canvas">

  <!-- Card: diagonal split -->
  <svg class="promo-card card-split" viewBox="0 0 433 288" aria-label="Promo card, diagonal split layout">
    <rect width="433" height="288" fill="var(--blush)"/>
    <polygon points="247,0 433,0 433,288 69,288" fill="var(--paper)"/>
    <text class="brand-name" x="135" y="153" font-size="30" text-anchor="middle">CORVID</text>
    <text class="display" x="256" y="126" font-size="66">15%</text>
    <text class="script" x="364" y="118" font-size="26">off</text>
    <text class="display" x="261" y="155" font-size="19">your purchase</text>
    <line x1="330" y1="168" x2="330" y2="190" stroke="var(--slate)" stroke-width="1.2"/>
    <rect x="260" y="190" width="140" height="36" fill="none" stroke="var(--slate)" stroke-width="1"/>
    <text class="display" x="330" y="213" font-size="14" text-anchor="middle">with code: MIRVOL</text>
    <text class="contact" x="400" y="254" text-anchor="end">www.corvidtpq.com</text>
    <text class="contact" x="400" y="267" text-anchor="end">@corvidtpq</text>
  </svg>

  <!-- Card: product chevron -->
  <svg class="promo-card card-product" viewBox="0 0 433 288" aria-label="Promo card with product image">
    <defs><clipPath id="productClip"><rect width="433" height="288"/></clipPath></defs>
    <rect width="433" height="288" fill="var(--blush)"/>
    <polygon points="0,0 125,0 210,143 110,288 0,288" fill="var(--paper)"/>
    <g clip-path="url(#productClip)">
      <circle cx="18" cy="18" r="94" fill="var(--slate)"/>
    </g>
    <rect role="img" aria-label="Product photo: plush pom-pom slippers in lilac and blush" x="3" y="98" width="165" height="100" rx="40" fill="var(--slipper)"/>
    <text class="display on-dark" x="22" y="66" font-size="46">15%</text>
    <text class="script on-dark" x="74" y="84" font-size="20">off</text>
    <text class="display" x="126" y="28" font-size="20">your</text>
    <text class="display" x="126" y="49" font-size="20">purchase</text>
    <text class="display" x="126" y="71" font-size="20">with code</text>
    <rect x="230" y="52" width="96" height="27" fill="none" stroke="var(--slate)" stroke-width="1"/>
    <text class="display" x="278" y="73" font-size="20" text-anchor="middle">MIRVOL</text>
    <g fill="var(--blush)">
      <circle cx="48" cy="202" r="2"/><circle cx="62" cy="202" r="2"/><circle cx="76" cy="202" r="2"/>
      <circle cx="48" cy="216" r="2"/><circle cx="62" cy="216" r="2"/><circle cx="76" cy="216" r="2"/>
    </g>
    <text class="brand-name" x="306" y="153" font-size="30" text-anchor="middle">CORVID</text>
    <g fill="var(--paper)">
      <circle cx="170" cy="246" r="2"/><circle cx="190" cy="246" r="2"/><circle cx="210" cy="246" r="2"/>
    </g>
    <text class="contact" x="400" y="250" text-anchor="end">www.corvidtpq.com</text>
    <text class="contact" x="400" y="263" text-anchor="end">@corvidtpq</text>
  </svg>

  <!-- Card: vertical brand with circle -->
  <svg class="promo-card card-circle" viewBox="0 0 433 288" aria-label="Promo card with vertical brand name">
    <defs><clipPath id="circleClip"><rect width="433" height="288"/></clipPath></defs>
    <rect width="433" height="288" fill="var(--blush)"/>
    <g clip-path="url(#circleClip)">
      <circle cx="342" cy="68" r="102" fill="var(--slate)"/>
    </g>
    <g fill="var(--paper)">
      <circle cx="220" cy="22" r="2"/><circle cx="234" cy="22" r="2"/>
      <circle cx="220" cy="36" r="2"/><circle cx="234" cy="36" r="2"/>
      <circle cx="220" cy="50" r="2"/><circle cx="234" cy="50" r="2"/>
    </g>
    <text class="brand-name" font-size="30" text-anchor="middle" transform="translate(82,144) rotate(-90)">CORVID</text>
    <text class="display on-dark" x="296" y="86" font-size="60">15%</text>
    <text class="script on-dark" x="384" y="84" font-size="24">off</text>
    <line x1="194" y1="110" x2="340" y2="110" stroke="var(--paper)" stroke-width="1.2"/>
    <text class="display on-dark" x="402" y="118" font-size="21" text-anchor="end">your</text>
    <text class="display on-dark" x="402" y="138" font-size="21" text-anchor="end">purchase</text>
    <text class="display" x="136" y="216" font-size="26">with code</text>
    <rect x="273" y="186" width="136" height="38" fill="none" stroke="var(--slate)" stroke-width="1"/>
    <text class="display" x="341" y="216" font-size="26" text-anchor="middle">MIRVOL</text>
    <g fill="var(--paper)">
      <circle cx="168" cy="246" r="2"/><circle cx="188" cy="246" r="2"/><circle cx="208" cy="246" r="2"/>
    </g>
    <text class="contact" x="400" y="250" text-anchor="end">www.corvidtpq.com</text>
    <text class="contact" x="400" y="263" text-anchor="end">@corvidtpq</text>
  </svg>

  <!-- Card: bold sans -->
  <svg class="promo-card card-bold" viewBox="0 0 433 288" aria-label="Promo card, bold sans layout">
    <rect width="433" height="288" fill="var(--blush)"/>
    <text class="headline" x="26" y="63" font-size="46">5% OFF</text>
    <text class="headline" x="26" y="89" font-size="22">YOUR PURCHASE</text>
    <text class="brand-name" x="212" y="152" font-size="32" text-anchor="middle">CORVID</text>
    <text class="headline" x="20" y="183" font-size="30">WITH</text>
    <text class="headline" x="20" y="222" font-size="30">CODE: <tspan fill="var(--slate)">MIRVOL</tspan></text>
    <text class="contact" x="216" y="252" text-anchor="middle">www.corvidtpq.com</text>
    <text class="contact" x="216" y="265" text-anchor="middle">@corvidtpq</text>
  </svg>

</main>
</body>
</html>
```